Flyer-Design für Immobilienhändler
Zielgruppe
Ich bin ein kleiner Immobilienhändler (nebenberuflich, meine Frau und ich, 2-Mann Unternehmen) und kaufe direkt Wohnimmobilen (Haus/Wohnungen) ein, um diese aufzuwerten und dann wieder zu verkaufen. Ich bin kein Makler, habe aber ähnliche Zielgruppen wie ein Makler, nur mit dem Unterschied das ich die Immos direkt kostenfrei kaufe so wie sie sind! Zielgruppe sind bei mir Privatpersonen (im mittlerem-höherem Alter 50-80 Jahre) die Ihre Immobilie verkaufen möchten.
Aufgabenstellung
Es soll ein Flyer sein mit folgenden Vorgaben:
• Design: Modern, einfach und wichtig ist das es professional und sehr seriös wirkt
• Auf den ersten Blick sollte die Message verständlich sein was ich suche und was die Vorteile sind es bei mir zu verkaufen, anstatt das einem Makler zu übergeben (siehe mein Entwurf).
• Flyer Format z.B. DIN A5/A6, was sich gut versenden lässt. Vorschläge sind willkommen
Im Anhang habe ein einen eigenen Entwurf beigefügt, jedoch bin offen für komplett neue Vorschläge was Text und Design angeht.

```html
<!DOCTYPE html>
<html lang="de">
<head>
<meta charset="utf-8">
<title>Hausweit – Flyer Ankauf</title>
<link href="https://fonts.googleapis.com/css2?family=Nunito:wght@600;800&family=Roboto+Condensed:wght@400;700&display=swap" rel="stylesheet">
<style>
:root{
  --teal:#006f79;
  --teal-dark:#005d66;
  --orange:#d35a2c;
  --ink:#2b2b2b;
  --paper:#ffffff;
  --stage-grey:#d9d9d9;
  --photo-grey:#e3e3e6;
  --rule:#c9c9c9;
}
*{box-sizing:border-box;margin:0;padding:0}
html,body{width:1200px;height:2400px;overflow:hidden;background:var(--paper)}
body{position:relative;font-family:"Roboto Condensed",Arial,sans-serif;color:var(--ink)}
.stage-top{position:absolute;left:0;top:0;width:1200px;height:662px;background:var(--stage-grey)}

.spread,.cover{position:absolute;transform-origin:0 0;box-shadow:0 4px 10px rgba(0,0,0,.22);overflow:hidden;background:var(--paper)}
.spread{width:966px;height:344px}
.cover{width:483px;height:344px}
.panel{position:absolute;top:0;width:483px;height:344px;overflow:hidden}
.panel--left{left:0}
.panel--right{left:483px}
.cover .panel{left:0}

.headline{font-family:"Nunito",Arial,sans-serif;font-weight:800;color:#fff;line-height:1.2}
.tag{display:inline-block;background:var(--teal);color:#fff;font-family:"Nunito",Arial,sans-serif;font-weight:800;font-size:14.5px;padding:1px 5px;margin-bottom:3px}

/* intro panel */
.intro-photo{position:absolute;left:24px;top:17px;width:439px;height:280px;background:linear-gradient(90deg,#e6e6e9 0%,#dedee1 55%,#c9c9cc 78%,#b3b4b7 100%)}
.intro-text{position:absolute;left:37px;top:34px;width:260px;font-size:8.6px;line-height:1.38}
.intro-text p{margin-top:9px}
.intro-text .tags{margin-bottom:6px}
.intro-text .sign{font-size:12px;margin-top:3px}
.web{position:absolute;font-size:7.5px;font-weight:700}

/* advantages panel */
.teal-panel{background:var(--teal)}
.adv-title{position:absolute;left:42px;top:48px;font-size:14.5px}
.adv-list{position:absolute;left:42px;top:112px;list-style:none;color:#fff;font-size:11.6px;line-height:23px}
.adv-list b{font-weight:700}

.badge{position:absolute;width:94px;height:94px;border-radius:50%;background:var(--orange);color:#fff;font-family:"Nunito",Arial,sans-serif;font-weight:800;font-size:9.5px;line-height:1.2;display:flex;flex-direction:column;justify-content:center;padding-left:14px;transform:rotate(-12deg)}
.badge .tel{margin-top:4px;letter-spacing:.5px}

/* back panel */
.hands-photo{position:absolute;left:0;top:0;width:245px;height:344px;background:radial-gradient(circle at 40% 45%,#e9c7a3 0%,#b98a5f 30%,#6e8a3c 60%,#4f7a2a 100%);border-radius:0 220px 220px 0/0 172px 172px 0}
.back-title{position:absolute;left:273px;top:40px;font-size:12.5px}
.back-text{position:absolute;left:272px;top:100px;color:#fff;font-size:8.6px;line-height:1.4}
.back-contact{position:absolute;left:272px;top:156px;color:#fff;font-size:8.6px;font-weight:700;line-height:1.45}
.back-contact span{display:inline-block;width:40px}
.brand{font-family:"Nunito",Arial,sans-serif;font-weight:600;letter-spacing:2.5px}
.back-brand{position:absolute;left:272px;top:282px;color:#fff;font-size:17px}

/* cover panel */
.couple-photo{position:absolute;left:0;top:0;width:483px;height:280px;background:linear-gradient(100deg,#d8d3c6 0%,#c8c0ae 35%,#9c8f61 60%,#6f7a33 80%,#8a6a2f 100%)}
.cover-rule{position:absolute;left:0;top:280px;width:483px;height:3px;background:var(--rule)}
.cover-title{position:absolute;left:266px;top:38px;font-size:15px;text-shadow:0 1px 2px rgba(0,0,0,.35)}
.perk{position:absolute;left:265px;width:160px;height:15px;background:var(--teal);color:#fff;font-size:8px;font-weight:700;line-height:15px;padding-left:20px}
.cover-brand{position:absolute;right:18px;top:306px;font-size:10.5px;color:var(--ink)}

.signoff-brand{position:absolute;left:0;top:2140px;width:1200px;text-align:center;font-size:52px;color:#222;letter-spacing:8px}
</style>
</head>
<body>

<div class="stage-top"></div>

<!-- Innenseite (Vorschau) -->
<section class="spread spread--inside" style="left:200px;top:190px;transform:scale(.828)">
  <div class="panel panel--left">
    <div class="intro-photo" role="img" aria-label="Foto: lächelnder Firmeninhaber mit Brille im grauen Sakko vor hellgrauem Hintergrund"></div>
    <div class="intro-text">
      <div class="tags"><span class="tag">Verkaufen ist Vertrauenssache.</span><br><span class="tag">Gerne stellen wir uns kurz vor:</span></div>
      <p>Als Familienunternehmen aus dem Rhein-Main-Gebiet haben wir uns darauf spezialisiert, gute und solide Immobilien zu kaufen. Direkt von den Eigentümern. <b>Ohne Renovierung. Ohne Sanierung. Ohne Belästigung durch Besichtigungen</b> für Sie.</p>
      <p>Da wir <b>keine Makler</b> sind, fallen für Sie <b>keinerlei Gebühren</b> an – den <b>Bestpreis</b> zahlen wir Ihnen dennoch.</p>
      <p>Gespannt, was wir Ihnen für Ihre Immobilie zahlen?<br>Wir freuen uns auf Ihre Anfrage!</p>
      <p>Herzliche Grüße,</p>
      <div class="sign">Martin Kessler</div>
    </div>
    <div class="web" style="left:388px;top:316px">www.hausweit-ankauf.de</div>
  </div>
  <div class="panel panel--right teal-panel">
    <h2 class="headline adv-title">6 Vielversprechende Vorteile, warum wir<br>der richtige Partner für Ihren Verkauf sind:</h2>
    <ol class="adv-list">
      <li>1. Abkauf direkt von uns, zum <b>fairen Bestpreis</b></li>
      <li>2. Professionelle, schnelle und <b>komplette Kaufabwicklung</b> aus einer Hand</li>
      <li>3. Sie brauchen nicht renovieren, sanieren oder entrümpeln</li>
      <li>4. Sie zahlen <b>keine Maklergebühr</b>,</li>
      <li>5. Sie haben <b>keinerlei Besucherstress</b></li>
      <li style="line-height:14px;margin-top:5px">6. Sie gehen <b>kein Haftungsrisiko</b> ein –<br>&nbsp;&nbsp;&nbsp;&nbsp;wir kaufen Ihre Immobilie so wie sie ist</li>
    </ol>
    <div class="badge" style="left:340px;top:220px">Jetzt völlig<br>unverbindlich<br>anfragen:<span class="tel">06123/480517</span></div>
  </div>
</section>

<!-- Titelseite (Vorschau) -->
<section class="cover" style="left:300px;top:705px;transform:scale(1.242)">
  <div class="panel">
    <div class="couple-photo" role="img" aria-label="Foto: lächelndes älteres Paar auf einer Holzbank im sonnigen Garten"></div>
    <div class="cover-rule"></div>
    <h1 class="headline cover-title">Beste Aussichten für<br>Ihren Immobilienverkauf –<br>und den besten Preis.</h1>
    <div class="perk" style="top:110px">keine Renovierung/Sanierung</div>
    <div class="perk" style="top:134px">kein Besichtigungsstress</div>
    <div class="perk" style="top:158px">keine Gebühren</div>
    <div class="badge" style="left:62px;top:216px">Jetzt völlig<br>unverbindlich<br>anfragen:<span class="tel">06123/480517</span></div>
    <div class="web" style="left:38px;top:320px">www.hausweit-ankauf.de</div>
    <div class="brand cover-brand">HAUSWEIT</div>
  </div>
</section>

<!-- Innenseite -->
<section class="spread spread--inside" style="left:150px;top:1200px;transform:scale(.932)">
  <div class="panel panel--left">
    <div class="intro-photo" role="img" aria-label="Foto: lächelnder Firmeninhaber mit Brille im grauen Sakko vor hellgrauem Hintergrund"></div>
    <div class="intro-text">
      <div class="tags"><span class="tag">Verkaufen ist Vertrauenssache.</span><br><span class="tag">Gerne stellen wir uns kurz vor:</span></div>
      <p>Als Familienunternehmen aus dem Rhein-Main-Gebiet haben wir uns darauf spezialisiert, gute und solide Immobilien zu kaufen. Direkt von den Eigentümern. <b>Ohne Renovierung. Ohne Sanierung. Ohne Belästigung durch Besichtigungen</b> für Sie.</p>
      <p>Da wir <b>keine Makler</b> sind, fallen für Sie <b>keinerlei Gebühren</b> an – den <b>Bestpreis</b> zahlen wir Ihnen dennoch.</p>
      <p>Gespannt, was wir Ihnen für Ihre Immobilie zahlen?<br>Wir freuen uns auf Ihre Anfrage!</p>
      <p>Herzliche Grüße,</p>
      <div class="sign">Martin Kessler</div>
    </div>
    <div class="web" style="left:388px;top:316px">www.hausweit-ankauf.de</div>
  </div>
  <div class="panel panel--right teal-panel">
    <h2 class="headline adv-title">6 Vielversprechende Vorteile, warum wir<br>der richtige Partner für Ihren Verkauf sind:</h2>
    <ol class="adv-list">
      <li>1. Abkauf direkt von uns, zum <b>fairen Bestpreis</b></li>
      <li>2. Professionelle, schnelle und <b>komplette Kaufabwicklung</b> aus einer Hand</li>
      <li>3. Sie brauchen nicht renovieren, sanieren oder entrümpeln</li>
      <li>4. Sie zahlen <b>keine Maklergebühr</b>,</li>
      <li>5. Sie haben <b>keinerlei Besucherstress</b></li>
      <li style="line-height:14px;margin-top:5px">6. Sie gehen <b>kein Haftungsrisiko</b> ein –<br>&nbsp;&nbsp;&nbsp;&nbsp;wir kaufen Ihre Immobilie so wie sie ist</li>
    </ol>
    <div class="badge" style="left:340px;top:220px">Jetzt völlig<br>unverbindlich<br>anfragen:<span class="tel">06123/480517</span></div>
  </div>
</section>

<!-- Außenseite -->
<section class="spread spread--outside" style="left:150px;top:1603px;transform:scale(.932)">
  <div class="panel panel--left teal-panel">
    <div class="hands-photo" role="img" aria-label="Foto: Hände übergeben ein kleines Hausmodell vor grünem Hintergrund"></div>
    <h2 class="headline back-title">Wenn es um<br>Immobilienverkauf geht.</h2>
    <p class="back-text">Sie wünschen ein unverbindliches Angebot?<br>Schreiben Sie uns oder rufen Sie an,<br>völlig unverbindlich und ohne Risiko:</p>
    <p class="back-contact"><span>Telefon:</span>06123 / 48 05 17<br><span>E-Mail:</span>kontakt@hausweit-ankauf.de</p>
    <div class="brand back-brand">HAUSWEIT</div>
  </div>
  <div class="panel panel--right">
    <div class="couple-photo" role="img" aria-label="Foto: lächelndes älteres Paar auf einer Holzbank im sonnigen Garten"></div>
    <div class="cover-rule"></div>
    <h1 class="headline cover-title">Beste Aussichten für<br>Ihren Immobilienverkauf –<br>und den besten Preis.</h1>
    <div class="perk" style="top:110px">keine Renovierung/Sanierung</div>
    <div class="perk" style="top:134px">kein Besichtigungsstress</div>
    <div class="perk" style="top:158px">keine Gebühren</div>
    <div class="badge" style="left:62px;top:216px">Jetzt völlig<br>unverbindlich<br>anfragen:<span class="tel">06123/480517</span></div>
    <div class="web" style="left:38px;top:320px">www.hausweit-ankauf.de</div>
    <div class="brand cover-brand">HAUSWEIT</div>
  </div>
</section>

<div class="brand signoff-brand">HAUSWEIT</div>

</body>
</html>
```